Kesselring sucht Cover
Herzlichen Dank an Seralie! Sie ist wirklich eine erstklassige Designerin! Ich habe mich sehr gut beraten gefühlt, Änderungen konnte ich zeitnah anschauen und auch die Kommunikation war perfekt.
Zielgruppe
Leser, die Spannung, aber auch die heiteren Aspekte eines Regionalkrimis lieben. Kein Thriller! Typischer Regiokrimi mit einem interessanten Ermittlerteam, Lokalkolorit und einer anstrengenden Liebesgeschichte zwischen Ermittler und Journalistin. Modern und sportlich (Protagonisten müssen in diesem Fall klettern) auf der einen Seite, psychischer Missbrauch auf der anderen. Spielt im Theatermilieu. Handlungszeitpunkt: Gegenwart.
Aufgabenstellung
Autorenname: Maren Pohlke (Mitte oben, klare Schrift)
Buchtitel: Kesselring und die stille Brandung (darunter)
Wobei "Kesselring" in Blockbuchstaben plakativ über die komplette Breite laufen soll - "und der tiefe Fall" kleiner darunter, eventuell Schriftbreite von Kesselring aufnehmen. Keine Blockbuchstaben. Moderne, krimitypische Schrift. Soll für eine Serie konzipiert sein. Die Unterüberschrift soll das Rot des Seidentuchs (siehe weiter unten) aufnehmen.
Im linken unteren Bereich bitte das Wort "Regionalkrimi" um 90 Grad gedreht und klein darstellen.
Farbgestaltung: Da es kein Thriller ist, bitte nicht zu dunkel. Eher helles Grau als Hintergrund. Im rechten unteren Bereich, ähnlich wie ein Lichtpunkt, Felsgestein als Hintergrund, verlaufend in den hellgrauen Hintergrund. Darüber schwebt ganz leicht ein knallrotes Seidentuch von links oben kommend. Falls es in die Schrift integriert werden kann, müsste die Unterüberschrift eventuell doch in einer anderen Farbe gestaltet werden. Das Tuch kann aber auch von unterhalb der Schrift kommend nach rechts unten und aus dem Cover hinaus segeln.
Hintergrund der Idee: Eine Frau in einem roten Kleid wird vom Felsen gestoßen. Bitte trotzdem keine echten Personen auf das Cover setzen.
Bild Ideensammlung 1: So in der Art, heller, Blickfang rechts unten, Schrift ohne Serifen, klarer
Bild Ideensammlung 2: Hintergrund eventuell passend, Ausrichtung Felsgestein rechts unten
Bild Ideensammlung 3: Idee für "Kesselring" - Buchstaben in unterschiedlicher Höhe

```html
<!DOCTYPE html>
<html lang="de">
<head>
<meta charset="utf-8">
<title>Kesselring und die stille Brandung – Cover</title>
<link rel="stylesheet" href="https://fonts.googleapis.com/css2?family=Bebas+Neue&family=Oswald:wght@500&display=swap">
<style>
  :root {
    --page-bg: #e9e9e8;
    --sky-light: #e6eff5;
    --sky-mid: #9cc3e0;
    --sky-deep: #3f7fb8;
    --rock-dark: #2b4560;
    --title-blue: #2c5590;
    --author-blue: #3b5570;
    --silk-red: #e0100f;
  }
  * { margin: 0; padding: 0; box-sizing: border-box; }
  html, body {
    width: 1200px; height: 800px; overflow: hidden;
    background: var(--page-bg);
  }
  .cover {
    position: absolute; left: 360px; top: 20px;
    width: 480px; height: 760px; overflow: hidden;
    box-shadow: 0 6px 24px rgba(0,0,0,0.18);
  }
  .cover-backdrop {
    position: absolute; inset: 0;
    background:
      radial-gradient(ellipse 70% 45% at 85% 95%, var(--rock-dark) 0%, rgba(43,69,96,0.6) 45%, rgba(43,69,96,0) 80%),
      linear-gradient(180deg, var(--sky-light) 0%, #d4e4ef 30%, var(--sky-mid) 55%, var(--sky-deep) 80%, #2f5f8e 100%);
  }
  .silk {
    position: absolute; left: 0; top: 0; width: 480px; height: 760px;
  }
  .author {
    position: absolute; top: 96px; left: 0; width: 100%;
    text-align: center;
    font-family: "Oswald", sans-serif; font-weight: 500;
    font-size: 46px; letter-spacing: 4px;
    color: var(--author-blue);
  }
  .title {
    position: absolute; top: 196px; left: 22px; right: 0;
    font-family: "Bebas Neue", sans-serif; font-weight: 400;
    color: var(--title-blue);
    text-transform: uppercase;
  }
  .title-main {
    display: block; font-size: 102px; line-height: 1;
    transform: scaleY(1.35); transform-origin: left top;
    letter-spacing: 1px;
  }
  .title-sub {
    display: block; margin-top: 52px;
    font-size: 44px; line-height: 1;
    transform: scaleY(1.45); transform-origin: left top;
    letter-spacing: 0.5px;
  }
  .genre {
    position: absolute; left: 40px; top: 640px;
    transform: rotate(-90deg); transform-origin: left top;
    font-family: "Oswald", sans-serif; font-weight: 500;
    font-size: 17px; letter-spacing: 3px;
    color: var(--title-blue);
    text-transform: uppercase;
  }
</style>
</head>
<body>
  <div class="cover">
    <div class="cover-backdrop" role="img" aria-label="Heller, wolkiger Himmel, der nach unten rechts in ein schneebedecktes Felsmassiv übergeht"></div>

    <div class="author">MAREN POHLKE</div>

    <svg class="silk" viewBox="0 0 480 760" role="img" aria-label="Knallrotes Seidentuch, das in Wellen quer über das Cover schwebt">
      <path fill="var(--silk-red)"
        d="M0 360
           C 15 300, 35 260, 50 262
           C 80 266, 110 420, 175 470
           C 230 510, 260 350, 300 338
           C 340 330, 360 520, 390 560
           C 420 520, 450 470, 480 450
           L 480 560
           C 450 580, 420 620, 385 630
           C 340 620, 320 420, 295 400
           C 260 420, 240 560, 175 545
           C 110 520, 70 360, 50 330
           C 35 330, 15 360, 0 400 Z"/>
    </svg>

    <h1 class="title">
      <span class="title-main">Kesselring</span>
      <span class="title-sub">und die stille Brandung</span>
    </h1>

    <div class="genre">Kriminalroman</div>
  </div>
</body>
</html>
```